MHT 25 year Anniversary - create file

I need an electronic Image file that I can incorporate into everything we are dong -including our pamphlets and brochures which we print in-house with Word Or Publisher files

The Vanto guide 25 file attached is the look we're after for part of our 25 year branding. I've included three of our different operating brands that should be incorporated into the letters. Other facts that can be included are :
123 combined years of experience
11792 Clients on file
11 Team Members
60% have been with us 5+ years
Service Entire Niagara Region
Carpet Cleaning
Oriental Rug Cleaning
Rug Binding
Making Custom Rugs
Winner of 8 Franchise Awards
Winner - Chamber of Commerce - "Summit Merit Honour"
Winner - Quillfen Promotions's "Climb past Limits " Award
Marisol and Tod featured in magazine article "Two Desks, One Home"
Supporters of the "Kids" programs at the KORB
Supporters of our Local Health System

Industry/Entity Type

Electronic

Colors
0255a3

Requirements
Must have
• final file must be a format that I can use to insert into other publications in Word and Publisher

```html
<!DOCTYPE html>
<html lang="en">
<head>
<meta charset="utf-8">
<title>MHT 25 Year Anniversary</title>
<link rel="stylesheet" href="https://fonts.googleapis.com/css2?family=Source+Sans+3:wght@400;600;700&display=swap">
<style>
  :root {
    --stage: #2b2b2b;
    --brand-blue: #0255a3;
    --brand-blue-light: #1f86d0;
    --numeral-fill: #ffffff;
    --numeral-shade: #e6ebf2;
    --numeral-edge: #2a2f78;
    --copy-blue: #0c55a3;
    --icon-grey: #707070;
    --tagline-dark: #111111;
    --band-white: #ffffff;
  }
  html, body {
    margin: 0;
    width: 1200px;
    height: 1000px;
    overflow: hidden;
    background: var(--stage);
  }
  .anniversary-card {
    position: absolute;
    left: 15px;
    top: 80px;
    width: 1170px;
    height: 840px;
    display: block;
  }
  .card text {
    font-family: "Source Sans 3", sans-serif;
    fill: var(--copy-blue);
  }
  .card .fact { text-anchor: middle; }
  .card .fact-figure { font-weight: 700; }
  .card .fact-label { font-weight: 400; }
  .card .fact-strong { font-weight: 700; }
  .card .brand-name { font-weight: 700; fill: var(--numeral-edge); text-anchor: middle; }
  .numeral {
    fill: url(#numeralFill);
    stroke: var(--numeral-edge);
    stroke-width: 2;
  }
  .icon-slot { fill: var(--icon-grey); }
  .badge-shape { fill: var(--icon-grey); }
  .card .tagline { font-weight: 700; fill: var(--tagline-dark); }
  .card .tagline-number { fill: var(--brand-blue); }
</style>
</head>
<body>
<svg class="anniversary-card card" viewBox="0 0 835 600" xmlns="http://www.w3.org/2000/svg" role="img" aria-label="MHT 25 years anniversary graphic">
  <defs>
    <radialGradient id="blueField" cx="50%" cy="50%" r="65%">
      <stop offset="0" stop-color="var(--brand-blue-light)"/>
      <stop offset="1" stop-color="var(--brand-blue)"/>
    </radialGradient>
    <linearGradient id="numeralFill" x1="0" y1="0" x2="0" y2="1">
      <stop offset="0" stop-color="var(--numeral-fill)"/>
      <stop offset="1" stop-color="var(--numeral-shade)"/>
    </linearGradient>
  </defs>

  <rect class="field" x="0" y="0" width="835" height="515" fill="url(#blueField)"/>

  <path class="numeral numeral-two" d="M72 486 L392 486 L392 412 L215 412 C300 350 395 280 395 175 C395 85 320 30 235 30 C140 30 75 90 72 175 L170 175 C172 140 200 110 235 110 C272 110 300 135 300 170 C300 235 215 315 72 412 Z"/>

  <path class="numeral numeral-five" d="M478 33 L750 33 L750 115 L555 115 L545 205 C570 195 600 190 625 190 C715 190 775 255 775 340 C775 430 700 490 610 490 C535 490 470 455 444 410 L444 345 L530 345 C540 385 568 410 600 410 C638 410 665 380 665 345 C665 308 638 280 600 280 C575 280 555 290 545 300 L458 300 Z"/>

  <!-- facts inside the two -->
  <text class="brand-name" x="225" y="66" font-size="24">MHT</text>

  <rect class="icon-slot" x="122" y="86" width="40" height="20" rx="4" role="img" aria-label="Handshake icon"/>
  <text class="fact fact-figure" x="130" y="140" font-size="25">11792</text>
  <text class="fact fact-label" x="128" y="155" font-size="14">Clients</text>
  <text class="fact fact-label" x="130" y="169" font-size="11">on file</text>

  <text class="fact fact-figure" x="320" y="92" font-size="28">11</text>
  <text class="fact fact-label" x="329" y="109" font-size="13">Team Members</text>
  <rect class="icon-slot" x="300" y="120" width="80" height="108" rx="6" role="img" aria-label="Grid of team member icons"/>

  <text class="fact fact-figure" x="306" y="268" font-size="30">60%</text>
  <text class="fact fact-label" x="282" y="285" font-size="15">have been</text>
  <text class="fact fact-label" x="270" y="302" font-size="15">with us</text>
  <text class="fact fact-strong" x="237" y="321" font-size="18">5+ years</text>

  <rect class="icon-slot" x="188" y="330" width="22" height="20" rx="3" role="img" aria-label="Thumbs up icon"/>
  <text class="fact fact-strong" x="174" y="371" font-size="16">Supporters</text>
  <text class="fact fact-label" x="158" y="387" font-size="14">of our Local</text>
  <text class="fact fact-label" x="142" y="403" font-size="14">Health System</text>

  <text class="fact fact-figure" x="135" y="441" font-size="28">123</text>
  <text class="fact fact-label" x="135" y="462" font-size="14">combined</text>
  <text class="fact fact-label" x="133" y="477" font-size="13">years of experience</text>

  <text class="fact fact-label" x="227" y="428" font-size="11">Making</text>
  <text class="fact fact-label" x="227" y="440" font-size="11">Custom Rugs</text>
  <rect class="icon-slot" x="258" y="437" width="58" height="26" rx="10" role="img" aria-label="Rolled rug icon"/>
  <text class="fact fact-label" x="347" y="430" font-size="11">Oriental Rug</text>
  <text class="fact fact-label" x="350" y="444" font-size="11">Cleaning</text>
  <text class="fact fact-label" x="235" y="478" font-size="11">Rug Binding</text>
  <text class="fact fact-label" x="340" y="478" font-size="11">Carpet Cleaning</text>

  <!-- facts inside the five -->
  <rect class="icon-slot" x="490" y="42" width="50" height="58" rx="4" role="img" aria-label="Trophy with stars"/>
  <text class="brand-name" x="600" y="68" font-size="15">Loomwell</text>
  <text class="brand-name" x="600" y="86" font-size="15">Gallery</text>
  <text class="brand-name" x="697" y="68" font-size="15">Fernbrook</text>
  <text class="brand-name" x="697" y="86" font-size="15">Rug Wash</text>

  <text class="fact fact-strong" x="514" y="132" font-size="19">Winner</text>
  <text class="fact fact-label" x="514" y="149" font-size="15">of 8</text>
  <text class="fact fact-label" x="514" y="166" font-size="15">Franchise</text>
  <text class="fact fact-label" x="514" y="183" font-size="15">Awards</text>

  <text class="fact fact-strong" x="514" y="210" font-size="19">Winner</text>
  <text class="fact fact-label" x="553" y="228" font-size="14">Quillfen Promotions's</text>
  <text class="fact fact-label" x="553" y="246" font-size="14">"Climb past Limits" Award</text>
  <circle class="badge-shape" cx="645" cy="202" r="13"/>

  <text class="fact fact-strong" x="694" y="248" font-size="19">Winner</text>
  <text class="fact fact-label" x="713" y="265" font-size="13">Chamber of</text>
  <text class="fact fact-label" x="713" y="281" font-size="13">Commerce</text>
  <text class="fact fact-label" x="713" y="297" font-size="13">"Summit Merit</text>
  <text class="fact fact-label" x="713" y="313" font-size="13">Honour"</text>
  <circle class="badge-shape" cx="719" cy="338" r="13"/>

  <text class="fact fact-label" x="715" y="380" font-size="13">Service Entire</text>
  <text class="fact fact-strong" x="715" y="396" font-size="13">Niagara</text>
  <text class="fact fact-label" x="715" y="412" font-size="13">Region</text>

  <text class="fact fact-label" x="494" y="362" font-size="13">Supporters</text>
  <text class="fact fact-label" x="494" y="378" font-size="13">of the "<tspan class="fact-strong">Kids</tspan>"</text>
  <text class="fact fact-label" x="494" y="394" font-size="13">programs</text>
  <text class="fact fact-label" x="494" y="410" font-size="13">at the KORB</text>
  <rect class="icon-slot" x="493" y="418" width="32" height="34" rx="4" role="img" aria-label="Two children icon"/>

  <text class="fact fact-strong" x="608" y="442" font-size="19">Marisol and Tod</text>
  <text class="fact fact-label" x="620" y="457" font-size="11">featured in magazine article</text>
  <text class="fact fact-strong" x="608" y="473" font-size="13">"Two Desks, One Home"</text>

  <!-- tagline band -->
  <rect class="tagline-band" x="0" y="515" width="835" height="85" fill="var(--band-white)"/>
  <text class="tagline" x="417" y="575" font-size="46" text-anchor="middle"><tspan class="tagline-number" font-size="56">25</tspan> years and just getting started!</text>
</svg>
</body>
</html>
```